361191

item 1. 8.5x11 1-side flyer design
item 2. 18x24 1-side poster design (also wants at 8.5x11)
item 3. 11x8.5 2-side brochure
design with Brookvale Healthcare brand standards similar to the job you did under 360565
see all attachments

```html
<!DOCTYPE html>
<html lang="en">
<head>
<meta charset="utf-8">
<title>Brookvale Healthcare – Syphilis Awareness Poster</title>
<link rel="stylesheet" href="https://fonts.googleapis.com/css2?family=Outfit:wght@400;500;600;700&display=swap">
<style>
  :root {
    --ink: #233a47;
    --sage: #7fa38c;
    --taupe: #aaa09b;
    --taupe-light: #b3aaa4;
    --body: #3a3d40;
    --paper: #ffffff;
    --backdrop: #8eadd6;
    --heart: #c8202b;
  }
  * { box-sizing: border-box; margin: 0; padding: 0; }
  html, body { width: 996px; height: 1200px; overflow: hidden; }
  body {
    background: var(--backdrop);
    font-family: "Outfit", sans-serif;
    color: var(--body);
  }
  .poster {
    position: absolute;
    left: 35px; top: 0;
    width: 926px; height: 1200px;
    background: var(--paper);
    overflow: hidden;
  }
  .abs { position: absolute; }

  /* Brand */
  .brand-name {
    left: 48px; top: 178px; width: 250px;
    color: var(--ink);
    font-weight: 500; font-size: 44px; line-height: 42px;
    text-align: center; letter-spacing: -1px;
  }
  .brand-mark {
    left: 130px; top: 62px; width: 100px; height: 100px;
    border-radius: 50%; background: var(--ink);
  }

  /* Headline */
  .headline-top {
    left: 300px; top: 52px;
    font-size: 100px; font-weight: 700; line-height: 1;
    color: var(--ink); letter-spacing: -4px;
  }
  .headline-band {
    left: 305px; top: 140px;
    background: var(--taupe);
    padding: 6px 18px 4px;
    transform: rotate(-3deg);
    color: #fff; font-weight: 600; font-size: 44px; line-height: 52px;
    letter-spacing: -1.5px;
    box-shadow: 0 8px 14px rgba(0,0,0,0.12);
  }
  .headline-bottom {
    left: 315px; top: 184px;
    font-size: 108px; font-weight: 600; line-height: 1;
    color: var(--sage); letter-spacing: -4px;
  }

  /* Doctor photo area */
  .halo { left: 470px; top: 270px; width: 480px; height: 460px; }
  .doctor-photo {
    left: 540px; top: 144px; width: 352px; height: 554px;
    border-radius: 170px 170px 6px 6px;
    background: linear-gradient(180deg, #efe9e4 0%, #e6ecf0 45%, #d8e3ee 100%);
  }
  .heart { border-radius: 50%; background: var(--heart); }
  .heart-big { left: 378px; top: 416px; width: 82px; height: 78px; }
  .heart-small { left: 498px; top: 540px; width: 48px; height: 46px; }

  /* Intro tear box */
  .intro { left: 49px; top: 303px; width: 530px; height: 148px; }
  .intro-text {
    left: 102px; top: 337px; width: 420px;
    color: #fff; font-weight: 500; font-size: 20px; line-height: 25px;
  }

  /* Stage pills */
  .pill {
    display: flex; align-items: center; justify-content: center;
    border-radius: 30px; color: #fff; font-weight: 500;
    font-size: 19px; letter-spacing: -0.3px;
  }
  .pill--ink { background: var(--ink); }
  .pill--sage { background: var(--sage); }
  .pill--taupe { background: var(--taupe); }

  .stage-primary { left: 46px; top: 486px; width: 234px; height: 53px; }
  .stage-secondary { left: 244px; top: 634px; width: 235px; height: 53px; }
  .stage-latent { left: 244px; top: 780px; width: 175px; height: 52px; }
  .stage-tertiary { left: 244px; top: 899px; width: 243px; height: 52px; }

  .check-item {
    display: flex; gap: 10px;
    font-size: 19px; line-height: 26px; color: var(--body);
  }
  .check-item svg { flex: none; margin-top: 4px; }
  .item-primary { left: 48px; top: 553px; width: 340px; }
  .item-secondary { left: 244px; top: 703px; width: 330px; }
  .item-latent { left: 244px; top: 847px; width: 330px; }
  .item-tertiary { left: 244px; top: 966px; width: 330px; }

  /* Rash photo */
  .rash-photo {
    left: 46px; top: 630px; width: 175px; height: 370px;
    background: linear-gradient(160deg, #ece9e7 0%, #e2b8a4 45%, #d69a85 100%);
  }

  /* Call to action bands */
  .cta {
    color: #fff; font-weight: 600; font-size: 35px; line-height: 1;
    display: flex; align-items: center; justify-content: center;
    letter-spacing: -0.5px;
  }
  .cta-get { left: 22px; top: 1000px; width: 232px; height: 62px; background: var(--sage); transform: rotate(1.5deg); }
  .cta-today { left: 56px; top: 1060px; width: 166px; height: 62px; background: var(--taupe); transform: rotate(-2deg); }

  /* Contact */
  .reach {
    left: 232px; top: 1095px; width: 120px;
    transform: rotate(-90deg); transform-origin: center;
    color: var(--ink); font-weight: 700; font-size: 25px; text-align: center;
  }
  .contact { left: 322px; top: 1060px; width: 260px; }
  .contact-row {
    display: flex; gap: 8px; align-items: flex-start;
    font-size: 17.5px; line-height: 21px; color: var(--ink);
    margin-bottom: 5px;
  }
  .contact-row svg { flex: none; margin-top: 3px; }

  /* Treatment panel */
  .panel {
    left: 594px; top: 695px; width: 289px; height: 461px;
    background: var(--ink); text-align: center;
  }
  .panel-title {
    margin-top: 72px;
    font-weight: 600; font-size: 35px; line-height: 41px; color: #fff;
    letter-spacing: -0.5px;
  }
  .panel-title span { color: var(--taupe-light); }
  .panel-pill {
    margin: 58px auto 0; width: 191px; height: 42px;
    font-size: 27px; font-weight: 600;
  }
  .prevention {
    margin-top: 26px; list-style: none;
    display: inline-block; text-align: left;
  }
  .prevention li {
    display: flex; gap: 9px; align-items: center;
    color: #fff; font-size: 17.5px; line-height: 25.5px;
  }
</style>
</head>
<body>
<main class="poster">

  <div class="abs brand-mark" aria-hidden="true"></div>
  <div class="abs brand-name">Brookvale<br>Healthcare</div>

  <svg class="abs halo" viewBox="0 0 480 460" aria-hidden="true">
    <path d="M 120 40 A 214 214 0 1 1 40 350" fill="none" stroke="var(--sage)" stroke-width="9"/>
  </svg>
  <div class="abs doctor-photo" role="img" aria-label="Photo of a masked doctor in a white coat with stethoscope, arms crossed"></div>

  <h1>
    <span class="abs headline-top">SYPHILIS</span>
    <span class="abs headline-bottom">RISE</span>
    <span class="abs headline-band">IS ON THE</span>
  </h1>

  <svg class="abs intro" viewBox="0 0 530 148" aria-hidden="true">
    <path d="M8 6 L40 2 L70 8 L110 3 L150 7 L200 2 L250 6 L300 1 L350 6 L400 2 L450 7 L500 3 L526 6 L520 40 L524 80 L518 118 L522 140 L480 144 L430 140 L380 146 L330 141 L280 146 L230 141 L180 146 L130 140 L80 146 L30 141 L2 145 L6 110 L0 70 L7 35 Z" fill="var(--taupe)"/>
  </svg>
  <p class="abs intro-text">Just because the symptoms go away doesn’t mean you’re cured without treatment.</p>

  <div class="abs heart heart-big" role="img" aria-label="Glossy red heart"></div>
  <div class="abs heart heart-small" role="img" aria-label="Small glossy red heart"></div>

  <div class="abs pill pill--ink stage-primary">Signs Primary Stage</div>
  <p class="abs check-item item-primary">
    <svg width="18" height="14" viewBox="0 0 18 14"><path d="M1 7 L6 12 L17 1" fill="none" stroke="var(--sage)" stroke-width="2.2"/></svg>
    <span>Sores called chancres on genitals or mouth.</span>
  </p>

  <div class="abs rash-photo" role="img" aria-label="Photo of a hand scratching an arm covered in a red skin rash"></div>

  <div class="abs pill pill--sage stage-secondary">Signs Primary Stage</div>
  <p class="abs check-item item-secondary">
    <svg width="18" height="14" viewBox="0 0 18 14"><path d="M1 7 L6 12 L17 1" fill="none" stroke="var(--sage)" stroke-width="2.2"/></svg>
    <span>Sore Throat, Weight Loss, Skin rashes, Joint pain, Fever, Fatigue.</span>
  </p>

  <div class="abs pill pill--taupe stage-latent">Latent Stage</div>
  <p class="abs check-item item-latent">
    <svg width="18" height="14" viewBox="0 0 18 14"><path d="M1 7 L6 12 L17 1" fill="none" stroke="var(--sage)" stroke-width="2.2"/></svg>
    <span>No Symptoms In Latent Stage.</span>
  </p>

  <div class="abs pill pill--ink stage-tertiary">Mouth Tertiary Stage</div>
  <p class="abs check-item item-tertiary">
    <svg width="18" height="14" viewBox="0 0 18 14"><path d="M1 7 L6 12 L17 1" fill="none" stroke="var(--sage)" stroke-width="2.2"/></svg>
    <span>Memory Loss, Deafness, Paralysis, Neurological problems.</span>
  </p>

  <div class="abs cta cta-get">GET TESTED</div>
  <div class="abs cta cta-today">TODAY!</div>

  <div class="abs reach">Reach Us!</div>
  <div class="abs contact">
    <p class="contact-row">
      <svg width="13" height="13" viewBox="0 0 24 24"><path d="M6.6 10.8a15.1 15.1 0 0 0 6.6 6.6l2.2-2.2a1 1 0 0 1 1-.25 11.4 11.4 0 0 0 3.6.57 1 1 0 0 1 1 1V20a1 1 0 0 1-1 1A17 17 0 0 1 3 4a1 1 0 0 1 1-1h3.5a1 1 0 0 1 1 1c0 1.25.2 2.45.57 3.57a1 1 0 0 1-.25 1z" fill="var(--sage)"/></svg>
      <span>(555) 214-7680</span>
    </p>
    <p class="contact-row">
      <svg width="13" height="13" viewBox="0 0 24 24"><path d="M4 2 L20 12 L13 13.5 L17 21 L14 22.5 L10 15 L4 20 Z" fill="var(--sage)"/></svg>
      <span>brookvalehealth.org</span>
    </p>
    <p class="contact-row">
      <svg width="13" height="15" viewBox="0 0 24 28"><path d="M12 1a9 9 0 0 0-9 9c0 7 9 17 9 17s9-10 9-17a9 9 0 0 0-9-9zm0 12.5A3.5 3.5 0 1 1 12 6.5a3.5 3.5 0 0 1 0 7z" fill="var(--sage)"/></svg>
      <span>1480 W. Pinecrest Ave<br>Ridgeford, AZ 85000</span>
    </p>
  </div>

  <section class="abs panel">
    <h2 class="panel-title">Treatment<br>Is Easy If<br><span>Caught Early!</span></h2>
    <div class="pill pill--sage panel-pill">Prevention</div>
    <ul class="prevention">
      <li><svg width="14" height="11" viewBox="0 0 18 14"><path d="M1 7 L6 12 L17 1" fill="none" stroke="var(--sage)" stroke-width="2.4"/></svg>Use Condoms</li>
      <li><svg width="14" height="11" viewBox="0 0 18 14"><path d="M1 7 L6 12 L17 1" fill="none" stroke="var(--sage)" stroke-width="2.4"/></svg>Avoid Recreational Drugs</li>
      <li><svg width="14" height="11" viewBox="0 0 18 14"><path d="M1 7 L6 12 L17 1" fill="none" stroke="var(--sage)" stroke-width="2.4"/></svg>Multiple Sex Partners</li>
    </ul>
  </section>

</main>
</body>
</html>
```